Cosmetic Clinic Looking For Sign Designs

We are looking for sign design ideas for the front of our building and a lawn sign for our cosmetic injection salon.
I have uploaded the front of our building for a mock up and size, lawn posts with size and a sign that uses the same dimensions.
We would like both signs to be black for the background.

Target Market(s)

Ages 18-75

Industry/Entity Type

Beauty

Requirements
Must have
• Services we offer:
• Cosmetic Injections
• Airbrush Spray Tanning
• Eyelash Growth Serum
• Skin Care Products & More
• Everything must be on a black background
• The lawn sign must have the address: 394 Fenwick and the building sign should have the phone number.
Should not have
• Nothing can light up (no LED)
• Both signs do not need the full address. Just 394 Fenwick and the phone number

```html
<!DOCTYPE html>
<html lang="en">
<head>
<meta charset="utf-8">
<title>Velvet Bloom Salon – Building Sign</title>
<link href="https://fonts.googleapis.com/css2?family=Roboto+Condensed:wght@400;700&display=swap" rel="stylesheet">
<style>
  :root {
    --sign-black: #000000;
    --wave-grey: #5a5a5a;
    --text-white: #ffffff;
    --accent-lavender: #7b7fbf;
    --accent-teal: #2299b8;
    --accent-pink: #e8187c;
  }
  html, body {
    margin: 0;
    padding: 0;
    width: 1200px;
    height: 273px;
    overflow: hidden;
    background: var(--sign-black);
  }
  .sign {
    position: relative;
    width: 1200px;
    height: 273px;
    background: var(--sign-black);
    font-family: "Roboto Condensed", "Arial Narrow", sans-serif;
    color: var(--text-white);
    overflow: hidden;
  }
  .wave-left, .wave-right {
    position: absolute;
    top: 0;
    height: 273px;
  }
  .wave-left {
    left: 0;
    width: 320px;
    background: radial-gradient(ellipse 260px 200px at 60px 40px, rgba(90,90,90,0.55), rgba(0,0,0,0) 75%);
  }
  .wave-right {
    right: 0;
    width: 460px;
    background: radial-gradient(ellipse 320px 150px at 330px 110px, rgba(90,90,90,0.45), rgba(0,0,0,0) 75%);
  }
  .services {
    position: absolute;
    left: 0;
    top: 93px;
    width: 272px;
    text-align: center;
  }
  .service {
    font-size: 19.5px;
    line-height: 1;
    margin: 0;
    white-space: nowrap;
  }
  .service-rule {
    width: 62px;
    height: 3px;
    margin: 8px auto 10px;
  }
  .rule-lavender { background: var(--accent-lavender); }
  .rule-teal { background: var(--accent-teal); }
  .rule-pink { background: var(--accent-pink); }
  .brand-mark {
    position: absolute;
    left: 538px;
    top: 23px;
    width: 124px;
    height: 124px;
    border-radius: 50%;
    background: var(--accent-lavender);
  }
  .brand-name {
    position: absolute;
    left: 400px;
    width: 400px;
    top: 165px;
    text-align: center;
    color: var(--accent-teal);
    font-weight: 700;
  }
  .brand-name-main {
    display: block;
    font-size: 56px;
    line-height: 56px;
    letter-spacing: 1px;
    white-space: nowrap;
  }
  .brand-name-sub {
    display: flex;
    align-items: center;
    justify-content: center;
    gap: 12px;
    font-size: 30px;
    line-height: 34px;
    letter-spacing: 1px;
    margin-top: 0;
  }
  .brand-rule {
    width: 91px;
    height: 3px;
    background: var(--accent-pink);
  }
  .contact {
    position: absolute;
    right: 26px;
    top: 192px;
    text-align: right;
    font-weight: 700;
    font-size: 20px;
    line-height: 32px;
  }
  .contact p { margin: 0; }
</style>
</head>
<body>
  <div class="sign">
    <div class="wave-left" role="img" aria-label="Soft grey flowing line waves"></div>
    <div class="wave-right" role="img" aria-label="Soft grey flowing line waves"></div>

    <div class="services">
      <p class="service">Cosmetic Injections</p>
      <div class="service-rule rule-lavender"></div>
      <p class="service">Airbrush Spray Tanning</p>
      <div class="service-rule rule-teal"></div>
      <p class="service">Eyelash Growth Serum</p>
      <div class="service-rule rule-pink"></div>
      <p class="service">Skin Care Products &amp; More</p>
    </div>

    <div class="brand-mark"></div>
    <div class="brand-name">
      <span class="brand-name-main">VELVET BLOOM</span>
      <span class="brand-name-sub"><span class="brand-rule"></span>SALON<span class="brand-rule"></span></span>
    </div>

    <div class="contact">
      <p>394 Fenwick</p>
      <p>+000 000 0000</p>
    </div>
  </div>
</body>
</html>
```